Digital Album Cover - Piano music for wedding ceremonies and receptions

I need cover art for a piano album project that will be distributed to TuneVault, Wavelane etc. Covert art required for front of album. At this stage physical CDs will not be printed nor required it is just a digital release.
Artist name: Toby Hargrove
Album Title: Gentle Keys Melodies Wedding Ceremonies and Receptions
Volume 3
Sample piano songs are on my tunecast page
https://tunecast.example/tobyhargrovekeys/sets/gentle-keys-melodies-vol-3
Previous album artwork used from sketch hive competitions winners
https://musicvault.example/au/artist/toby-hargrove/4830917265
Target Market(s)
brides to be
grooms to be
people interested in weddings
people enjoy love songs or easy listening music
Industry/Entity Type
Wedding
Look and feel
Each slider illustrates characteristics of the customer's brand and the style your logo design should communicate.

```html
<!DOCTYPE html>
<html lang="en">
<head>
<meta charset="utf-8">
<title>Toby Hargrove – Gentle Keys Melodies, Volume 3</title>
<link href="https://fonts.googleapis.com/css2?family=Tinos:ital@1&display=swap" rel="stylesheet">
<style>
  :root {
    --page: #ffffff;
    --navy: #222632;
    --gold: #b48c64;
    --band: #c39a6e;
    --ivory: #ffffff;
    --bloom-light: #efe6dc;
    --bloom-peach: #d9b8a0;
    --leaf: #5d6b48;
    --wood: #4a2a24;
  }
  html, body {
    margin: 0;
    width: 1200px;
    height: 1200px;
    overflow: hidden;
    background: var(--page);
  }
  .album-cover {
    position: absolute;
    left: 190px;
    top: 189px;
    width: 820px;
    height: 820px;
    background: var(--navy);
    overflow: hidden;
    font-family: "Tinos", "Times New Roman", serif;
    font-style: italic;
  }
  .cover-art {
    position: absolute;
    inset: 0;
    width: 820px;
    height: 820px;
  }
  .cover-text {
    position: absolute;
    right: 38px;
    margin: 0;
    line-height: 1;
    font-weight: 400;
    text-align: right;
    white-space: nowrap;
  }
  .artist-name { top: 47px; font-size: 56px; color: var(--ivory); }
  .album-title { top: 105px; font-size: 66px; color: var(--gold); }
  .album-subtitle { top: 185px; font-size: 45px; color: var(--ivory); }
  .album-subtitle-2 { top: 230px; font-size: 45px; color: var(--ivory); }
  .volume-label {
    position: absolute;
    left: 14px;
    top: 763px;
    margin: 0;
    font-size: 38px;
    line-height: 1;
    color: var(--ivory);
  }
</style>
</head>
<body>
  <main class="album-cover">
    <svg class="cover-art" viewBox="0 0 820 820" xmlns="http://www.w3.org/2000/svg">
      <defs>
        <linearGradient id="bouquetTones" x1="0" y1="0" x2="1" y2="1">
          <stop offset="0" stop-color="var(--bloom-peach)"/>
          <stop offset="0.35" stop-color="var(--bloom-light)"/>
          <stop offset="0.6" stop-color="var(--leaf)"/>
          <stop offset="0.8" stop-color="#cfcac2"/>
          <stop offset="1" stop-color="var(--wood)"/>
        </linearGradient>
      </defs>
      <path class="photo-area" role="img" aria-label="Photograph of a bouquet of cream and peach roses resting on piano keys"
            d="M0,222 Q636,338 816,820 L0,820 Z" fill="url(#bouquetTones)"/>
      <path class="gold-band" d="M0,219 Q640,336 820,820" fill="none" stroke="var(--band)" stroke-width="7"/>
      <path class="volume-tab" d="M0,712 Q0,706 10,708 L150,752 Q170,760 180,778 L202,820 L0,820 Z" fill="var(--navy)"/>
    </svg>
    <h1 class="cover-text artist-name">TOBY HARGROVE</h1>
    <h2 class="cover-text album-title">Gentle Keys Melodies</h2>
    <p class="cover-text album-subtitle">Wedding Ceremonies</p>
    <p class="cover-text album-subtitle-2">and Receptions</p>
    <p class="volume-label">Volume 3</p>
  </main>
</body>
</html>
```